Web Design for an Online Dating Web Site

We need an uncoded web design for a new online dating web site called zMatchy.net. Simplicity and boldness are the key factors in the successful design.
Please look at the requirements document attached for details.
Updates
Dear all,
Please AVOID USING A PICTURE OF A HAPPY COUPLE ON THE HOME PAGE of the site. We highly want to move away from this space as it makes our web site just like another dating web site.
We like something simple with web 2.0 look and feel. The examples in the Requirements Document are exactly the design we are after.
Regards
Tarn
Industry/Entity Type
Dating
Look and feel
Each slider illustrates characteristics of the customer's brand and the style your logo design should communicate.

```html
<!DOCTYPE html>
<html lang="en">
<head>
<meta charset="utf-8">
<title>zMatchy.net – My Friends</title>
<link href="https://fonts.googleapis.com/css2?family=Ubuntu:wght@400;500;700&family=Arimo:wght@400;700&display=swap" rel="stylesheet">
<style>
:root{
  --pink:#e2007a;
  --pink-dark:#c8006b;
  --pink-deep:#b8005f;
  --night:#26292d;
  --blue:#0b86b8;
  --sky:#8ad4ec;
  --line:#d9d9d9;
}
*{box-sizing:border-box;margin:0;padding:0}
html,body{width:1200px;height:1200px;overflow:hidden}
body{position:relative;background:radial-gradient(ellipse at 50% 0,#45484d 0,#2c2f33 45%,var(--night) 100%);font-family:Arimo,Arial,sans-serif;color:#333}
.abs{position:absolute}
.brand{left:0;width:1200px;top:30px;text-align:center;font-family:Ubuntu,sans-serif;font-weight:700;font-size:50px;line-height:56px;color:var(--pink);letter-spacing:-1px}
.brand .dot{display:inline-block;width:14px;height:14px;border-radius:50%;background:var(--pink);margin-left:6px;vertical-align:middle}
.brand small{display:block;font-size:11px;font-weight:400;line-height:12px;color:#8a8d92;letter-spacing:0;margin-top:-6px;padding-left:120px}
.page{left:246px;top:126px;width:711px;height:829px;background:#fff}
.mainnav{left:0;top:0;width:711px;height:58px;background:linear-gradient(#2f3236,#24272a);display:flex}
.mainnav a{width:109px;height:58px;border-right:1px dashed #4a4d52;color:#eee;font-family:Ubuntu,sans-serif;font-size:11.5px;text-align:center;text-decoration:none;padding-top:5px;position:relative}
.mainnav a svg{display:block;margin:0 auto 3px;width:30px;height:30px}
.mainnav a.active{background:var(--pink)}
.mainnav a.active::after{content:"";position:absolute;left:50%;bottom:0;margin-left:-4px;border:4px solid transparent;border-bottom-color:#24272a}
.userbox{flex:1;display:flex;align-items:center;padding-left:9px;font-family:Georgia,serif;font-size:10px;color:#eee;line-height:12px}
.userbox .avatar{width:36px;height:36px;background:linear-gradient(135deg,#bbb,#555);border:2px solid #ddd;margin-right:13px}
.userbox .new{color:var(--pink)}
.userbox .caret{margin-left:18px;border:5px solid transparent;border-top-color:#eee;margin-top:6px}
.subnav{left:0;top:58px;width:711px;height:29px;background:linear-gradient(#e8308f,var(--pink-dark));display:flex}
.subnav a{height:29px;border-right:1px dashed #f07ab8;color:#fff;font-family:Ubuntu,sans-serif;font-size:11px;text-align:center;line-height:29px;text-decoration:none}
.subnav a.active{background:#fff;color:var(--pink);font-weight:700;border:0;position:relative}
.subnav a.active::after{content:"";position:absolute;left:50%;bottom:0;margin-left:-4px;border:4px solid transparent;border-bottom-color:var(--pink)}
.section-head{left:156px;top:100px}
.section-head h1{position:absolute;left:61px;top:0;font-family:Ubuntu,sans-serif;font-weight:400;font-size:22px;color:var(--pink);white-space:nowrap}
.section-head p{position:absolute;left:61px;top:30px;width:345px;font-size:10.5px;line-height:13px;color:#777}
.dots{left:0;width:711px;border-top:1px dotted #c9c9c9}
.username{left:26px;top:188px;font-weight:700;font-size:18px;color:var(--blue)}
.username span{font-size:10.5px;font-weight:400;color:#888}
.video{left:22px;top:220px;width:480px;height:298px;box-shadow:0 3px 8px rgba(0,0,0,.35)}
.video .still{width:480px;height:269px;background:linear-gradient(135deg,#3b2f26 0,#8a7460 35%,#b89c86 55%,#d9d4cc 80%,#e9e6e0 100%)}
.video .play{position:absolute;left:170px;top:70px}
.controls{position:absolute;left:0;top:269px;width:480px;height:29px;background:linear-gradient(#f2f2f2,#cfcfcf);display:flex;align-items:center;font-size:9px;color:#555}
.bar{height:8px;border-radius:4px;background:#666;position:relative}
.bar i{position:absolute;left:0;top:0;height:8px;border-radius:4px;background:var(--pink);display:block}
.bar b{position:absolute;top:-2px;width:12px;height:12px;border-radius:50%;background:#eee;border:1px solid #999}
.tags{left:522px;top:224px;width:175px}
.tags h3,.contact h3{font-size:9.5px;color:var(--pink);font-weight:700}
.tags ul{list-style:none;display:flex;flex-wrap:wrap;gap:3px 6px;margin-top:10px}
.tags li{background:var(--blue);color:#fff;font-size:8.5px;font-weight:700;line-height:11px;border-radius:8px;padding:2px 7px;border:1px solid #06709b}
.taglist-line{left:519px;top:310px;width:177px;border-top:1px solid var(--line)}
.contact{left:521px;top:319px;width:171px;height:158px;background:#ededed;border:1px solid #cfcfcf;border-radius:2px;padding:8px 7px}
.btn{border-radius:13px;font-family:Ubuntu,sans-serif;font-weight:700;font-size:15px;text-align:center;line-height:25px}
.btn-woo{left:604px;top:491px;width:88px;height:28px;background:linear-gradient(#fff,#e3e3e3);border:1px solid #bbb;color:var(--pink);border-radius:6px}
.btn-friends{left:302px;top:536px;width:108px;height:25px;background:linear-gradient(#f0409a,var(--pink-dark));color:#fff}
.btn-next{left:427px;top:536px;width:75px;height:25px;background:linear-gradient(#fff,#e5e5e5);border:1px solid #bbb;color:#777;line-height:23px}
.comments-title{left:27px;top:589px;font-size:9.5px;color:var(--pink)}
.comments-title b{font-weight:700}
.comment{left:28px;width:658px;height:62px;border-top:1px solid var(--line);font-size:8px;color:#333}
.comment .pic{position:absolute;left:1px;top:14px;width:30px;height:30px;background:#666;color:#fff;font-weight:700;font-size:10px;text-align:center;line-height:30px;border:1px solid #ccc}
.comment .pic.light{background:#ddd}
.comment .who{position:absolute;left:38px;top:15px;font-weight:700;font-size:8.5px}
.comment .who small{display:block;font-weight:400;font-size:7px;color:#999;margin-top:2px}
.comment .text{position:absolute;left:103px;top:14px;width:545px;line-height:11px}
.footer{left:0;top:955px;width:1200px;height:245px;background:var(--pink);border-top:2px dotted #f36fb4}
.col-title{font-weight:700;font-size:18px;color:var(--sky);width:210px;padding-bottom:8px;border-bottom:1px solid #f28cc4}
.readmore{left:247px;top:20px}
.readmore ul{list-style:none;margin-top:13px;font-size:10px;font-weight:700;color:#fff;line-height:12px}
.talk{left:496px;top:20px}
.field{width:158px;height:18px;background:var(--pink-deep);color:#fff;font-size:9px;font-weight:700;padding:4px 7px;border-radius:2px}
.field.area{width:204px;height:84px}
.send{width:94px;height:19px;background:#3a3a3a;color:#fff;font-size:9px;font-weight:700;text-align:center;line-height:19px;border-radius:2px}
.foot-brand{left:744px;top:20px}
.foot-brand .name{font-family:Ubuntu,sans-serif;font-weight:700;font-size:24px;color:#fff;width:210px;padding-bottom:4px;border-bottom:1px solid #f28cc4}
.foot-brand .name i{display:inline-block;width:9px;height:9px;border-radius:50%;background:#fff;margin-left:4px}
.social{position:absolute;top:64px;left:0;display:grid;grid-template-columns:repeat(4,16px);gap:4px 3px}
.social i{width:16px;height:16px;background:#f7f7f7;border-radius:2px;opacity:.9;display:block}
.counter{position:absolute;left:114px;display:flex;align-items:center;font-size:8px}
.counter span:first-child{width:50px;height:13px;background:#e9f3f8;border-radius:2px}
.counter span:last-child{background:#fff;color:#333;padding:1px 4px;margin-left:3px;border:1px solid #ccc}
</style>
</head>
<body>

<div class="abs brand">zMatchy<span class="dot"></span><small>zmatchy.net</small></div>

<main class="abs page">
  <nav class="abs mainnav">
    <a class="active" href="#"><svg viewBox="0 0 30 30"><circle cx="11" cy="11" r="6" fill="none" stroke="#fff" stroke-width="4" stroke-dasharray="3 2"/><circle cx="21" cy="21" r="4" fill="none" stroke="#fff" stroke-width="3" stroke-dasharray="2 1.5"/></svg>My Stuff</a>
    <a href="#"><svg viewBox="0 0 30 30"><rect x="5" y="7" width="17" height="14" fill="none" stroke="#fff" stroke-width="2.2" transform="rotate(-30 13 14)"/><circle cx="23" cy="16" r="6" fill="var(--pink)" stroke="#fff" stroke-width="1.5"/><text x="23" y="19" font-size="8" fill="#fff" text-anchor="middle" font-family="Arial">1</text></svg>My Messages</a>
    <a href="#"><svg viewBox="0 0 30 30"><path d="M13 24 L4 14 A5 5 0 0 1 13 8 A5 5 0 0 1 22 14 Z" fill="none" stroke="#fff" stroke-width="2.2"/><path d="M22 27 L17 22 A2.7 2.7 0 0 1 22 19 A2.7 2.7 0 0 1 27 22 Z" fill="none" stroke="#fff" stroke-width="1.8"/></svg>Start Dating</a>
    <a href="#"><svg viewBox="0 0 30 30"><path d="M13 24 L4 14 A5 5 0 0 1 13 8 A5 5 0 0 1 22 14 Z" fill="none" stroke="#fff" stroke-width="2.2"/><path d="M16 15 L26 25 M26 19 V25 H20" fill="none" stroke="#fff" stroke-width="2.2"/></svg>Sign Out</a>
    <a href="#"><svg viewBox="0 0 30 30"><circle cx="12" cy="11" r="7" fill="none" stroke="#fff" stroke-width="2.5"/><path d="M17 16 L25 26" stroke="#fff" stroke-width="4"/></svg>Help</a>
    <div class="userbox"><div class="avatar"></div><div>Wed. 7th Oct 2011<br>Hello Username !<br><span class="new">1 new message !</span></div><div class="caret"></div></div>
  </nav>
  <nav class="abs subnav">
    <a href="#" style="width:143px">My Details</a>
    <a href="#" style="width:142px">My Seeking Criteria</a>
    <a href="#" style="width:142px">My Avatar</a>
    <a href="#" style="width:142px">My Video</a>
    <a href="#" class="active" style="width:142px">My Friends</a>
  </nav>

  <div class="abs section-head">
    <svg width="50" height="52" viewBox="0 0 50 52" style="position:absolute;left:0;top:0"><circle cx="18" cy="12" r="8" fill="none" stroke="var(--pink)" stroke-width="3.5"/><circle cx="32" cy="16" r="7" fill="none" stroke="var(--pink)" stroke-width="3.5"/><path d="M4 48 V40 A14 14 0 0 1 32 40 V48 Z" fill="none" stroke="var(--pink)" stroke-width="3.5"/><path d="M34 26 A12 12 0 0 1 46 38 V46 H36" fill="none" stroke="var(--pink)" stroke-width="3.5"/></svg>
    <h1>My Friends</h1>
    <p>Lorem ipsum dolor sit amet, consectetur adipiscing elit. Donec ipsum sem, pretium vel blandit dictum, sodales et metus.</p>
  </div>
  <div class="abs dots" style="top:172px"></div>

  <div class="abs username">Username <span>Lorem ipsum dolor sit amet</span></div>

  <div class="abs video">
    <div class="still" role="img" aria-label="Video still of the member's profile recording"></div>
    <svg class="play" width="120" height="120" viewBox="0 0 120 120"><circle cx="60" cy="60" r="54" fill="none" stroke="rgba(255,255,255,.55)" stroke-width="7"/><path d="M48 36 L84 60 L48 84 Z" fill="rgba(255,255,255,.45)"/></svg>
    <div class="controls">
      <svg width="40" height="29" viewBox="0 0 40 29"><path d="M13 9 L23 14.5 L13 20 Z" fill="#555"/></svg>
      <div class="bar" style="width:222px"><i style="width:110px"></i><b style="left:103px"></b></div>
      <span style="margin-left:8px">3.47 / 9.29</span>
      <svg width="30" height="29" viewBox="0 0 30 29" style="margin-left:6px"><path d="M6 12 H10 L15 8 V21 L10 17 H6 Z" fill="#555"/><path d="M18 11 Q21 14.5 18 18" stroke="#555" fill="none"/></svg>
      <div class="bar" style="width:54px"><b style="left:44px"></b></div>
      <svg width="40" height="29" viewBox="0 0 40 29"><rect x="16" y="9" width="10" height="10" fill="none" stroke="#555" stroke-width="1.5"/></svg>
    </div>
  </div>

  <div class="abs tags">
    <h3>Tags</h3>
    <ul><li>Short Tag</li><li>Tag</li><li>Longest Tag</li><li>Tag</li><li>Short Tag</li><li>Tag</li><li>Longest Tag</li><li>Short Tag</li></ul>
  </div>
  <div class="abs taglist-line"></div>
  <div class="abs contact"><h3>Contact Me</h3></div>
  <div class="abs btn btn-woo">Woo Me !</div>
  <div class="abs btn btn-friends">Be friends !</div>
  <div class="abs btn btn-next">Next ▸</div>

  <div class="abs dots" style="top:577px"></div>
  <div class="abs comments-title"><b>Comments about</b> Username</div>

  <div class="abs comment" style="top:612px">
    <div class="pic">?</div>
    <div class="who">Korvel 218<small>22 hours ago</small></div>
    <div class="text">Lorem ipsum dolor sit amet, consectetur adipiscing elit. Nulla consequat, nunc eget tincidunt mattis, sapien ante malesuada lectus, a bibendum eros leo eu urna. Nunc viverra ultricies felis eget semper..</div>
  </div>
  <div class="abs comment" style="top:674px">
    <div class="pic light" role="img" aria-label="Member avatar"></div>
    <div class="who">Pipalune<small>4 days ago</small></div>
    <div class="text">Nam at velit sit amet erat gravida congue non vel sapien.</div>
  </div>
  <div class="abs comment" style="top:736px">
    <div class="pic">?</div>
    <div class="who">BrightFen<small>5 days ago</small></div>
    <div class="text">Lorem ipsum dolor sit amet, consectetur adipiscing elit. Nulla consequat, nunc eget tincidunt mattis, sapien ante malesuada lectus, a bibendum eros leo eu urna. Nunc viverra ultricies felis eget semper..</div>
  </div>
</main>

<footer class="abs footer">
  <div class="abs readmore">
    <div class="col-title">Read More</div>
    <ul><li>Why zMatchy</li><li>How it works</li><li>Sign Up</li><li>Login</li><li>About Us</li></ul>
  </div>
  <div class="abs talk">
    <div class="col-title">Let’s Talk</div>
    <div class="field" style="margin-top:13px">Name</div>
    <div class="field" style="margin-top:8px">Email</div>
    <div class="field area" style="margin-top:8px">Comments</div>
    <div class="send" style="margin-top:9px">Send the message</div>
  </div>
  <div class="abs foot-brand">
    <div class="name">zMatchy<i></i></div>
    <div class="social"><i></i><i></i><i></i><i></i><i></i><i></i><i></i><i></i></div>
    <i style="position:absolute;left:88px;top:64px;width:16px;height:16px;background:#f7f7f7;border-radius:2px"></i>
    <div class="counter" style="top:65px"><span></span><span>6,314</span></div>
    <div class="counter" style="top:84px"><span style="background:#5a6fa8"></span><span>377</span></div>
  </div>
</footer>

</body>
</html>
```